Business Card design for a company called Tallow Flame NI

I need a business card design for my oil fired boiler servicing company. I have a logo design already and Im just looking that incorporated into the business card design. card details; Tallow Flame NI
Oil Burner Servicing - Mid Ulster Area
Service Engineer - Owen Marsh
Mobile 07751364927
email - Tallow.Flame.NI@hearthmail.example
www.tallowflameni.example
I carry out Servicing, Commissioning, Fault Finding, Warranty Validation
Target Market(s)
home owners with oil fired central heating
Industry/Entity Type
Business
Contact Information for Business Card
Tallow Flame NI
Tell. 07751364927
Web: www.tallowflameni.example
email Tallow.Flame.NI@Hearthmail.Example
Servicing Fault Finding Commissioning Warranty Validation
Look and feel

```html
<!DOCTYPE html>
<html lang="en">
<head>
<meta charset="utf-8">
<title>Tallow Flame NI – Business Card</title>
<link rel="stylesheet" href="https://fonts.googleapis.com/css2?family=Open+Sans:wght@400;700&family=Caladea:wght@700&display=swap">
<style>
  :root {
    --page-bg: #e9e7e4;
    --card-bg: #141414;
    --card-edge: #1f1f1f;
    --brand-green: #7ac943;
    --bright-green: #8fd14f;
    --text-white: #f2f2f2;
  }
  * { box-sizing: border-box; margin: 0; padding: 0; }
  html, body {
    width: 1200px; height: 780px; overflow: hidden;
    background: var(--page-bg);
  }
  body {
    display: flex; align-items: center; justify-content: center;
    font-family: "Open Sans", Arial, sans-serif;
  }
  .business-card {
    position: relative;
    width: 1000px; height: 600px;
    background: radial-gradient(ellipse at 40% 30%, #1c1c1c 0%, var(--card-bg) 70%);
    border: 1px solid var(--card-edge);
    box-shadow: 0 12px 30px rgba(0,0,0,.25);
    overflow: hidden;
  }
  .brand {
    position: absolute; left: 70px; top: 58px;
    display: flex; align-items: center; gap: 34px;
  }
  .brand-mark {
    width: 130px; height: 130px; border-radius: 50%;
    background: var(--brand-green);
    flex: none;
  }
  .brand-name {
    font-weight: 700; font-size: 70px; line-height: 1;
    color: var(--brand-green); letter-spacing: 1px;
  }
  .brand-tagline {
    margin-top: 14px;
    font-size: 19px; letter-spacing: 3.2px; text-transform: uppercase;
    color: var(--brand-green);
  }
  .engineer {
    position: absolute; right: 110px; top: 290px; text-align: left;
  }
  .engineer-name {
    font-family: "Caladea", Georgia, serif; font-weight: 700;
    font-size: 56px; line-height: 1; color: var(--bright-green);
  }
  .engineer-role {
    font-size: 36px; color: var(--text-white); margin-top: 2px; margin-left: 8px;
  }
  .contact-list {
    position: absolute; left: 110px; top: 348px;
    list-style: none;
  }
  .contact-item {
    display: flex; align-items: center; gap: 22px;
    font-size: 29px; line-height: 40px; color: var(--text-white);
  }
  .contact-icon { width: 22px; height: 22px; flex: none; }
  .services {
    position: absolute; left: 0; right: 0; top: 486px;
    display: flex; align-items: center;
  }
  .services-rule {
    height: 2px; background: var(--brand-green);
  }
  .services-rule.lead { width: 80px; align-self: flex-start; margin-top: 4px; }
  .services-rule.tail { flex: 1; align-self: flex-end; margin-bottom: 2px; margin-left: 10px; }
  .services-text {
    font-size: 31px; color: var(--text-white); white-space: nowrap; padding-left: 20px; padding-top: 12px;
  }
</style>
</head>
<body>
  <article class="business-card">
    <header class="brand">
      <span class="brand-mark" aria-hidden="true"></span>
      <div>
        <div class="brand-name">Tallow Flame NI</div>
        <div class="brand-tagline">Oil Burner Servicing - Mid Ulster Area</div>
      </div>
    </header>

    <section class="engineer">
      <div class="engineer-name">Owen Marsh</div>
      <div class="engineer-role">Service Engineer</div>
    </section>

    <ul class="contact-list">
      <li class="contact-item">
        <svg class="contact-icon" viewBox="0 0 22 22" aria-label="Phone"><rect width="22" height="22" rx="3" fill="#7ac943"/><path d="M7 5c1 0 1.5 2 1.5 3S7.5 9 7.5 10s2.5 4 3.5 4 1-1.3 2-1.3 3 .5 3 1.5-1.5 2.8-3 2.8C9 17 5 12.5 5 8c0-1.5 1-3 2-3z" fill="#141414"/></svg>
        07751364927
      </li>
      <li class="contact-item">
        <svg class="contact-icon" viewBox="0 0 22 22" aria-label="Email"><rect width="22" height="22" rx="3" fill="#7ac943"/><rect x="4" y="6.5" width="14" height="9.5" fill="#141414"/><path d="M4.5 7l6.5 5 6.5-5" stroke="#7ac943" stroke-width="1.4" fill="none"/></svg>
        Tallow.Flame.NI@Hearthmail.Example
      </li>
      <li class="contact-item">
        <svg class="contact-icon" viewBox="0 0 22 22" aria-label="Website"><rect width="22" height="22" rx="3" fill="#7ac943"/><circle cx="11" cy="11" r="6.5" fill="none" stroke="#141414" stroke-width="1.6"/><ellipse cx="11" cy="11" rx="2.8" ry="6.5" fill="none" stroke="#141414" stroke-width="1.4"/><path d="M4.5 11h13" stroke="#141414" stroke-width="1.4"/></svg>
        www.tallowflameni.example
      </li>
    </ul>

    <footer class="services">
      <span class="services-rule lead"></span>
      <span class="services-text">Servicing Fault Finding Commissioning Warranty Validation</span>
      <span class="services-rule tail"></span>
    </footer>
  </article>
</body>
</html>
```